Loyalty/Gift Card Design-

Pumlavo needs a design for a loyalty card for a retail gas discount program. The card will need to fit specifications for brenvoxa cards cr-80 magnetic card found on www.brenvoxa.com

The way our program works is a consumer will see advertisement for our program and come to a local gas station to purchase our Pumlavo Card. It will be a set price up- front, then our program/card will save consumers 15 cents per gallon on 100 gallons of fuel. Once the 100 gallons is used the customer will have the option of reloading (for another set cost) another 100 gallons on the card to receive another 15 cents off on next 100 gallons.

Key Info to Incorporate on card--
"Save 15 cents per gallon on next 100 gallons of fuel"
Never pay full price on fuel again!
"Card Valid Only At" (then a space for our stores name and address)
Brought to you by-- Pumlavo Name & Logo

Target Market(s)

Consumers conscious of gas prices/ economy who are looking to save money where they can. We are looking for a design that fits "big box" theme, with very clean design.

Industry/Entity Type

Gas Station

Requirements
Must have
• Colors Red,, Blue, White--
Sell Message of Saving and Value.
Should not have
• Designs with fuel pumps

```html
<!DOCTYPE html>
<html lang="en">
<head>
<meta charset="utf-8">
<title>Pumlavo Fuel Savings Card</title>
<link rel="stylesheet" href="https://fonts.googleapis.com/css2?family=Open+Sans:ital,wght@0,400;0,600;0,700;1,400&display=swap">
<style>
  :root {
    --page: #ffffff;
    --card-light: #ffd23a;
    --card-mid: #fcbf1e;
    --card-deep: #f5a313;
    --band: #f9ea1c;
    --band-edge: #e9c90f;
    --headline-red: #f21414;
    --outline-red: #e0191b;
    --outline-dark: #2a0606;
    --white: #ffffff;
    --ink: #111111;
    --brand-blue: #1f2fb8;
    --art-green: rgba(150, 200, 130, 0.55);
    --art-red: rgba(220, 40, 30, 0.55);
    --art-orange: rgba(236, 120, 40, 0.6);
  }
  * { margin: 0; padding: 0; box-sizing: border-box; }
  html, body {
    width: 1200px; height: 800px; overflow: hidden;
    background: var(--page);
    font-family: "Open Sans", Arial, sans-serif;
  }
  .canvas { position: relative; width: 1200px; height: 800px; }
  .card {
    position: absolute; left: 36px; top: 43px; width: 1131px; height: 718px;
    border-radius: 36px; overflow: hidden;
    background: radial-gradient(circle at 88% 22%, var(--card-light) 0%, var(--card-mid) 45%, var(--card-deep) 100%);
  }
  .fuel-art {
    position: absolute; left: 470px; top: 250px; width: 661px; height: 357px;
    border-radius: 180px 0 0 60px;
    background: linear-gradient(110deg, var(--art-green) 0%, var(--art-red) 40%, var(--art-orange) 80%, rgba(236,120,40,0.3) 100%);
  }
  .headline {
    position: absolute; left: 0; width: 100%; text-align: center; white-space: nowrap; line-height: 1;
  }
  .headline--offer {
    top: 60px; font-size: 36px; font-weight: 600; color: var(--white);
    -webkit-text-stroke: 2px var(--outline-red); paint-order: stroke fill;
    text-shadow: 0 0 4px var(--outline-red), 0 0 2px var(--outline-red);
  }
  .headline--promise {
    top: 154px; font-size: 65px; font-weight: 700; color: var(--headline-red);
    text-shadow: 0 0 3px var(--outline-dark), 0 0 6px rgba(42,6,6,.8), 0 0 14px rgba(255,255,255,.6);
    letter-spacing: -0.5px;
  }
  .valid-at {
    position: absolute; left: 35px; top: 442px; line-height: 1;
    font-size: 25px; color: var(--white);
  }
  .sponsor-band {
    position: absolute; left: 0; top: 607px; width: 100%; height: 63px;
    background: var(--band);
    border-top: 1px solid var(--band-edge); border-bottom: 2px solid var(--band-edge);
    display: flex; align-items: center; padding-left: 19px;
  }
  .sponsor-band__label { font-size: 25px; color: var(--ink); }
  .sponsor-band__name {
    margin-left: 38px; font-size: 25px; font-style: italic; color: var(--brand-blue);
  }
  .brand-mark {
    position: absolute; left: 642px; top: 600px; height: 76px;
    display: flex; align-items: center; gap: 16px;
  }
  .brand-mark__square {
    width: 70px; height: 70px; background: var(--brand-blue); border-radius: 8px;
  }
  .brand-mark__name {
    font-size: 64px; font-weight: 700; color: var(--brand-blue); line-height: 1;
  }
</style>
</head>
<body>
<div class="canvas">
  <div class="card">
    <div class="fuel-art" role="img" aria-label="Illustration of an arm holding a fuel nozzle that sprays banknotes"></div>
    <p class="headline headline--offer">"Save 15 cents per gallon on next 100 gallons of fuel"</p>
    <p class="headline headline--promise">Never pay full price on fuel again!</p>
    <p class="valid-at">Card Valid Only At :</p>
    <div class="sponsor-band">
      <span class="sponsor-band__label">Brought to you by :</span>
      <span class="sponsor-band__name">Pumlavo</span>
    </div>
    <div class="brand-mark">
      <span class="brand-mark__square"></span>
      <span class="brand-mark__name">Pumlavo</span>
    </div>
  </div>
</div>
</body>
</html>
```